Commercial Construction Company

We need a business card design based on our current logo. We are a commercial general contractor based in Southern California that specializes in bank remodels. We would like to see designs that incorporate dark blue. The final design should portray an image of professionalism and quality.

If possible, I would like to add metallic foil to the design. Thank you

```html
<!DOCTYPE html>
<html lang="en">
<head>
<meta charset="utf-8">
<title>Halvern Business Card</title>
<link rel="stylesheet" href="https://fonts.googleapis.com/css2?family=Montserrat:wght@500;700;800&display=swap">
<style>
  :root {
    --stage: #6e6e70;
    --card-white: #f2f2f2;
    --ink: #161616;
    --panel-dark: #1c1c1e;
    --panel-dark-top: #3a3a3c;
    --blue-light: #4f8fdc;
    --blue-deep: #2f4f8a;
    --rule-grey: #3a3a3a;
    --arc-grey: #5f5f62;
    --accent-grey: #8a8a8c;
    --muted-text: #d6d6d6;
  }
  * { margin: 0; padding: 0; box-sizing: border-box; }
  html, body {
    width: 1200px;
    height: 800px;
    overflow: hidden;
    background: var(--stage);
    font-family: "Montserrat", Arial, sans-serif;
  }
  .stage {
    width: 1200px;
    height: 800px;
    display: flex;
    align-items: center;
    justify-content: center;
    gap: 40px;
  }
  .card {
    width: 560px;
    height: 320px;
    position: relative;
    overflow: hidden;
    background: var(--card-white);
    box-shadow: 0 10px 24px rgba(0,0,0,0.35);
  }
  .card-art {
    position: absolute;
    inset: 0;
    width: 100%;
    height: 100%;
  }
  /* Contact side */
  .contact-list {
    position: absolute;
    right: 24px;
    top: 26px;
    list-style: none;
    color: var(--card-white);
  }
  .contact-item {
    display: flex;
    align-items: center;
    justify-content: flex-end;
    gap: 18px;
    margin-bottom: 20px;
  }
  .contact-text { text-align: right; }
  .contact-name { font-weight: 800; font-size: 15px; letter-spacing: 0.2px; }
  .contact-role { font-weight: 500; font-size: 10px; color: var(--muted-text); margin-top: 2px; }
  .contact-line { font-weight: 700; font-size: 14px; }
  .contact-icon { width: 32px; height: 32px; flex: none; }
  .contact-web {
    position: absolute;
    right: 96px;
    bottom: 38px;
    color: var(--card-white);
    font-weight: 700;
    font-size: 14px;
  }
  .brand-small {
    position: absolute;
    left: 34px;
    top: 222px;
    display: flex;
    align-items: center;
    gap: 10px;
  }
  .brand-name {
    font-weight: 800;
    color: var(--ink);
    letter-spacing: 1px;
  }
  .brand-small .brand-name { font-size: 24px; }
  .brand-dot {
    width: 14px;
    height: 14px;
    border-radius: 50%;
    background: var(--blue-deep);
  }
  /* Brand side */
  .brand-large {
    position: absolute;
    left: 260px;
    top: 128px;
    display: flex;
    align-items: center;
    gap: 12px;
  }
  .brand-large .brand-name { font-size: 40px; }
  .brand-large .brand-dot { width: 20px; height: 20px; }
</style>
</head>
<body>
<main class="stage">

  <section class="card card--contact" aria-label="Business card, contact side">
    <svg class="card-art" viewBox="0 0 560 320" aria-hidden="true">
      <defs>
        <linearGradient id="contactBlue" x1="0" y1="0" x2="0.4" y2="1">
          <stop offset="0" stop-color="#5a8bd8"/>
          <stop offset="1" stop-color="#2a4f9c"/>
        </linearGradient>
        <linearGradient id="contactDark" x1="0" y1="0" x2="0.3" y2="1">
          <stop offset="0" stop-color="var(--panel-dark-top)"/>
          <stop offset="1" stop-color="var(--panel-dark)"/>
        </linearGradient>
      </defs>
      <rect width="560" height="320" fill="var(--card-white)"/>
      <polygon points="0,0 560,0 560,320 345,320 0,110" fill="url(#contactBlue)"/>
      <polygon points="228,0 560,0 560,320 368,320 170,180" fill="url(#contactDark)"/>
      <line x1="0" y1="106" x2="346" y2="320" stroke="var(--rule-grey)" stroke-width="5"/>
    </svg>

    <ul class="contact-list">
      <li class="contact-item">
        <div class="contact-text">
          <p class="contact-name">Your Name</p>
          <p class="contact-role">Director</p>
        </div>
        <svg class="contact-icon" viewBox="0 0 32 32" aria-hidden="true">
          <circle cx="16" cy="9" r="6" fill="var(--card-white)"/>
          <path d="M3 30 C3 20 9 17 16 17 C23 17 29 20 29 30 Z" fill="var(--card-white)"/>
        </svg>
      </li>
      <li class="contact-item">
        <p class="contact-line">+1 555 0139 4870</p>
        <svg class="contact-icon" viewBox="0 0 32 32" aria-hidden="true">
          <path d="M9 5 L14 11 L11 14 C13 18 15 20 19 22 L22 19 L28 24 L24 29 C14 28 5 19 4 9 Z" fill="var(--card-white)"/>
          <path d="M18 4 A10 10 0 0 1 28 14" fill="none" stroke="var(--card-white)" stroke-width="2.5" stroke-linecap="round"/>
          <path d="M18 9 A5 5 0 0 1 23 14" fill="none" stroke="var(--card-white)" stroke-width="2.5" stroke-linecap="round"/>
        </svg>
      </li>
      <li class="contact-item">
        <p class="contact-line">Your company address here</p>
        <svg class="contact-icon" viewBox="0 0 32 32" aria-hidden="true">
          <path d="M16 31 C10 22 5 17 5 12 A11 11 0 0 1 27 12 C27 17 22 22 16 31 Z" fill="var(--card-white)"/>
          <circle cx="16" cy="12" r="4.5" fill="var(--panel-dark)"/>
        </svg>
      </li>
    </ul>
    <p class="contact-web">www.yoursite.com</p>

    <div class="brand-small">
      <span class="brand-dot"></span>
      <span class="brand-name">HALVERN</span>
    </div>
  </section>

  <section class="card card--brand" aria-label="Business card, brand side">
    <svg class="card-art" viewBox="0 0 560 320" aria-hidden="true">
      <defs>
        <linearGradient id="brandBlue" x1="0" y1="0" x2="0.3" y2="1">
          <stop offset="0" stop-color="var(--blue-light)"/>
          <stop offset="1" stop-color="var(--blue-deep)"/>
        </linearGradient>
      </defs>
      <rect width="560" height="320" fill="url(#brandBlue)"/>
      <path d="M172 0 L560 0 L560 320 L320 320 L110 186 C106 120 125 50 172 0 Z" fill="var(--card-white)"/>
      <path d="M172 0 L238 0 C180 30 130 100 122 192 L110 186 C106 120 125 50 172 0 Z" fill="var(--arc-grey)"/>
      <rect x="530" y="178" width="30" height="22" fill="var(--accent-grey)"/>
    </svg>

    <div class="brand-large">
      <span class="brand-dot"></span>
      <span class="brand-name">HALVERN</span>
    </div>
  </section>

</main>
</body>
</html>
```